Business Card Design Project

We're an orthopaedic office, and our colors are blue white and balck. Dealing with physicians and healthcare execs, I'd like this card to have a classy, yet overpowering wow factor.

Here are a couple of cards I like that are close to what I'm looking for:
http://www.pixelbazaro.com/design/392047
http://www.pixelbazaro.com/design/286390

Industry/Entity Type

Healthcare

```html
<!DOCTYPE html>
<html lang="en">
<head>
<meta charset="utf-8">
<title>Crestview Orthopaedic – Business Card</title>
<link href="https://fonts.googleapis.com/css2?family=Questrial&display=swap" rel="stylesheet">
<style>
  :root {
    --backdrop: #1f1f21;
    --card-blue: #2c34a8;
    --card-blue-deep: #232a92;
    --ink-white: #ffffff;
    --ink-soft: rgba(255,255,255,0.85);
    --rule: rgba(255,255,255,0.55);
  }
  * { box-sizing: border-box; margin: 0; padding: 0; }
  html, body {
    width: 1200px; height: 900px; overflow: hidden;
    background: var(--backdrop);
    font-family: "Questrial", "Century Gothic", sans-serif;
    color: var(--ink-white);
  }
  .canvas { position: relative; width: 1200px; height: 900px; }

  .card {
    position: absolute;
    width: 560px; height: 320px;
    background: linear-gradient(135deg, var(--card-blue) 0%, var(--card-blue-deep) 100%);
    box-shadow: 0 18px 40px rgba(0,0,0,0.55);
  }
  .card--back { left: 110px; top: 100px; }
  .card--front { left: 530px; top: 480px; }

  /* Back side */
  .brand-block {
    position: absolute; left: 40px; top: 0; bottom: 0; width: 190px;
    display: flex; align-items: center; gap: 12px;
  }
  .brand-dot { width: 30px; height: 30px; border-radius: 50%; background: var(--ink-white); flex: none; }
  .brand-word { font-size: 24px; letter-spacing: 1px; line-height: 1; }

  .contact-block {
    position: absolute; left: 250px; top: 92px;
    padding-left: 16px; border-left: 1px solid var(--rule);
  }
  .person-name { font-size: 17px; letter-spacing: 1.5px; text-transform: uppercase; }
  .person-title { font-size: 11px; letter-spacing: 1px; color: var(--ink-soft); margin-bottom: 10px; }
  .contact-list { list-style: none; }
  .contact-item {
    display: flex; align-items: center; gap: 7px;
    font-size: 12px; line-height: 19px; color: var(--ink-soft); letter-spacing: 0.4px;
  }
  .contact-icon { width: 12px; height: 12px; flex: none; }

  /* Front side */
  .front-lockup {
    position: absolute; left: 0; right: 0; top: 58px;
    display: flex; flex-direction: column; align-items: center; text-align: center;
  }
  .front-dot { width: 56px; height: 56px; border-radius: 50%; background: var(--ink-white); margin-bottom: 18px; }
  .front-name { font-size: 50px; line-height: 1; letter-spacing: 1px; text-transform: uppercase; }
  .front-line { font-size: 28px; line-height: 1.15; letter-spacing: 1px; text-transform: uppercase; }
  .front-sub { font-size: 22px; line-height: 1.2; letter-spacing: 1px; }
</style>
</head>
<body>
<main class="canvas">

  <section class="card card--back" aria-label="Business card back">
    <div class="brand-block">
      <span class="brand-dot"></span>
      <span class="brand-word">CRESTVIEW</span>
    </div>
    <div class="contact-block">
      <p class="person-name">Dalton Reyes</p>
      <p class="person-title">CEO</p>
      <ul class="contact-list">
        <li class="contact-item">
          <svg class="contact-icon" viewBox="0 0 12 12"><rect width="12" height="12" rx="2" fill="#fff"/><path d="M3.5 3c.6 2.6 2.4 4.6 5 5.5l.8-1.2-1.4-.8-.6.6C6.2 6.6 5.4 5.8 5 4.8l.6-.6-.8-1.4z" fill="#2c34a8"/></svg>
          (555) 201-4470
        </li>
        <li class="contact-item">
          <svg class="contact-icon" viewBox="0 0 12 12"><rect width="12" height="12" rx="2" fill="#fff"/><rect x="2.5" y="3.5" width="7" height="5" fill="none" stroke="#2c34a8"/><path d="M2.5 3.5 6 6.3 9.5 3.5" fill="none" stroke="#2c34a8"/></svg>
          dreyes@crestviewortho.com
        </li>
        <li class="contact-item">
          <svg class="contact-icon" viewBox="0 0 12 12"><rect width="12" height="12" rx="2" fill="#fff"/><circle cx="6" cy="6" r="3.4" fill="none" stroke="#2c34a8"/><path d="M2.6 6h6.8M6 2.6c-1.6 2-1.6 4.8 0 6.8M6 2.6c1.6 2 1.6 4.8 0 6.8" fill="none" stroke="#2c34a8" stroke-width=".7"/></svg>
          www.crestviewortho.com
        </li>
        <li class="contact-item">
          <svg class="contact-icon" viewBox="0 0 12 12"><rect width="12" height="12" rx="2" fill="#fff"/><path d="M6 10S3.2 6.9 3.2 5a2.8 2.8 0 0 1 5.6 0C8.8 6.9 6 10 6 10z" fill="#2c34a8"/><circle cx="6" cy="5" r="1" fill="#fff"/></svg>
          1820 Harbor Ln. Fairview, LA 70412
        </li>
      </ul>
    </div>
  </section>

  <section class="card card--front" aria-label="Business card front">
    <div class="front-lockup">
      <span class="front-dot"></span>
      <p class="front-name">Crestview</p>
      <p class="front-line">Orthopaedic &amp; Sports</p>
      <p class="front-sub">Medicine Center</p>
    </div>
  </section>

</main>
</body>
</html>
```